Korvalin Solutions needs mailable brochure design

We need a brochure design that we can mail via the post office (trifold), plus mail online (html format). We would like the brochure to highlight on the services we are offering. We would like the colors to match those that are in our logo which is attached. I've included some text in addition to jpeg images that you may want to consider using. The transfer fees we refer to in the text is related to geophysical seismic data

Target Market(s)

Energy companies

Industry/Entity Type

Oil And Gas

```html
<!DOCTYPE html>
<html lang="en">
<head>
<meta charset="utf-8">
<title>Korvalin Solutions – Trifold Brochure</title>
<link rel="stylesheet" href="https://fonts.googleapis.com/css2?family=Montserrat:wght@400;500;700;800&family=Lato:wght@700&display=swap">
<style>
  :root {
    --page-bg: #bcbdbf;
    --brand-red: #d93a27;
    --brand-blue: #4387c6;
    --brand-navy: #163b60;
    --panel-dark: #221f24;
    --white: #ffffff;
  }
  html, body {
    margin: 0;
    width: 1200px;
    height: 1000px;
    overflow: hidden;
    background: var(--page-bg);
    font-family: "Montserrat", Arial, sans-serif;
  }
  .brochure {
    position: absolute;
    left: 85px;
    top: 100px;
    width: 1030px;
    height: 800px;
    display: grid;
    grid-template-columns: 336px 340px 354px;
    grid-template-rows: 226px 266px 308px;
    background: var(--white);
  }
  .tile { position: relative; overflow: hidden; }

  .tagline {
    background: var(--brand-red);
    color: var(--white);
    display: flex;
    align-items: center;
    justify-content: center;
    text-align: center;
  }
  .tagline p {
    margin: 0;
    font-size: 25px;
    font-weight: 500;
    line-height: 31px;
    letter-spacing: 0.2px;
  }

  .photo-archive-room { background: linear-gradient(180deg, #efeee9 0%, #d8d3c4 45%, #c9c3b3 60%, #ebe9e3 100%); }
  .photo-pumpjack { background: linear-gradient(180deg, #6d9ed0 0%, #a9c8e4 45%, #d4dbe0 62%, #b5a06a 72%, #8d8a45 100%); }
  .photo-server-hall { background: linear-gradient(180deg, #d9d8f0 0%, #a9a8e0 35%, #7e7fcf 55%, #cfcff0 80%, #e8e8f7 100%); }
  .photo-tape-library { background: linear-gradient(180deg, #15151a 0%, #2a2930 40%, #3a3a42 55%, #15151a 100%); }

  .brand-mark {
    background: var(--white);
    display: flex;
    align-items: center;
    justify-content: center;
    gap: 10px;
    color: var(--brand-navy);
    font-family: "Lato", Arial, sans-serif;
    font-weight: 700;
  }
  .brand-mark--stacked { flex-direction: column; gap: 18px; padding-top: 10px; }
  .brand-mark--stacked .brand-dot { width: 88px; height: 88px; }
  .brand-mark--stacked .brand-name { font-size: 38px; letter-spacing: 0.5px; }
  .brand-mark--inline .brand-dot { width: 44px; height: 44px; }
  .brand-mark--inline .brand-name { font-size: 23px; }
  .brand-dot { display: block; border-radius: 50%; background: var(--brand-red); }

  .contact {
    background: var(--panel-dark);
    color: var(--white);
    text-align: center;
    padding-top: 36px;
    box-sizing: border-box;
  }
  .contact h2 { margin: 0 0 24px; font-size: 24px; font-weight: 700; letter-spacing: 0.3px; }
  .contact address { font-style: normal; font-size: 14px; line-height: 19px; }
  .contact .lines { margin: 18px 0 0; font-size: 14px; line-height: 19px; }
  .contact .lines b { font-weight: 800; }
  .contact .web { margin-top: 22px; font-size: 11px; letter-spacing: 0.3px; }

  .services {
    background: var(--brand-blue);
    color: var(--white);
    text-align: center;
  }
  .services h2 {
    margin: 86px 0 0;
    font-size: 26px;
    font-weight: 700;
    line-height: 31.5px;
    letter-spacing: 0.3px;
  }
  .services .web { position: absolute; left: 0; right: 0; top: 260px; font-size: 11px; letter-spacing: 0.3px; }
</style>
</head>
<body>
  <main class="brochure">
    <section class="tile tagline">
      <p>Korvalin can provide<br>the aide to mitigate<br>financial and<br>operational exposure.</p>
    </section>
    <div class="tile photo-archive-room" role="img" aria-label="Photo of a bright archive room with rows of storage racks"></div>
    <section class="tile brand-mark brand-mark--stacked">
      <span class="brand-dot" aria-hidden="true"></span>
      <span class="brand-name">KORVALIN</span>
    </section>

    <div class="tile photo-pumpjack" role="img" aria-label="Photo of an oil pumpjack and storage tanks on a grassy field under blue sky"></div>
    <section class="tile contact">
      <h2>CONTACT US</h2>
      <address>1180 Meridian Park<br>Sealy, Tx&nbsp; 77401</address>
      <p class="lines">
        <b>Telephone:</b> 1+ (281)555-0167<br>
        <b>Fax:</b> 1+ (281)555-0168<br>
        <b>E-mail:</b> mail@korvalin.com
      </p>
      <div class="web">www.KORVALIN.COM</div>
    </section>
    <div class="tile photo-server-hall" role="img" aria-label="Photo of a glowing data center corridor lined with server cabinets"></div>

    <section class="tile brand-mark brand-mark--inline">
      <span class="brand-dot" aria-hidden="true"></span>
      <span class="brand-name">KORVALIN</span>
    </section>
    <div class="tile photo-tape-library" role="img" aria-label="Close-up photo of a data tape library with rows of labelled cartridges"></div>
    <section class="tile services">
      <h2>DATA DRIVEN<br>BUSINESS AND<br>TECHNOLOGY<br>SOLUTIONS</h2>
      <div class="web">www.korvalin.com</div>
    </section>
  </main>
</body>
</html>
```